Book Cover

Book cover for a study guide on Galatians. The title would be: "Unbound Hearts: Called Out to Walk Open" Possibly using a bird breaking free from a cage.+

Target Market(s)

We will sell them to our church.

Requirements
Must have
• Authors are Dr. Martin Oskerby and Dr. Helen Oskerby

```html
<!DOCTYPE html>
<html lang="en">
<head>
<meta charset="utf-8">
<title>Unbound Hearts – Book Cover Wrap</title>
<link rel="stylesheet" href="https://fonts.googleapis.com/css2?family=Dancing+Script:wght@600&family=Marcellus&family=Crimson+Text&display=swap">
<style>
  :root {
    --navy: #3c3e5b;
    --pink: #e2b4d6;
    --blush: #f6e2e4;
    --rose-line: #e7b9dc;
    --cream: #f1efdc;
    --cream-text: #efedc8;
    --white-soft: #fbf4f4;
    --frame: #9a9a9a;
    --art-tint: rgba(226, 180, 214, 0.32);
    --art-tint-soft: rgba(246, 226, 228, 0.18);
  }
  html, body { margin: 0; padding: 0; overflow: hidden; background: #fff; }
  .canvas {
    position: relative; width: 1200px; height: 735px; overflow: hidden;
    background: #fff; box-sizing: border-box; border: 1px solid var(--frame);
  }
  .flap { position: absolute; left: 0; top: 0; }
  .panel { position: absolute; top: 83px; height: 633px; background: var(--navy); }
  .panel--back { left: 50px; width: 481px; }
  .panel--spine { left: 538px; width: 124px; }
  .panel--front { left: 669px; width: 481px; }

  .art {
    position: absolute; border-radius: 6px;
    background: linear-gradient(135deg, var(--art-tint), var(--art-tint-soft));
  }

  .script-title {
    position: absolute; margin: 0; white-space: nowrap;
    font-family: "Dancing Script", cursive; font-weight: 600;
    background: linear-gradient(90deg, var(--pink), var(--blush));
    -webkit-background-clip: text; background-clip: text; color: transparent;
    line-height: 1.2;
  }
  .subtitle {
    position: absolute; margin: 0; white-space: nowrap;
    font-family: "Marcellus", serif; line-height: 1;
  }

  /* back */
  .back-title { left: 40px; top: 196px; width: 400px; text-align: center; font-size: 62px; }
  .back-subtitle { left: 100px; top: 280px; width: 300px; text-align: center; font-size: 23px; color: var(--pink); }
  .bio { position: absolute; left: 80px; width: 400px; }
  .bio__label { margin: 0 0 4px; font-family: "Marcellus", serif; font-size: 12px; color: var(--pink); line-height: 1; }
  .bio__name { margin: 0 0 5px; font-family: "Marcellus", serif; font-size: 23px; font-weight: 400; color: var(--pink); line-height: 1.05; }
  .bio__text { margin: 0; font-family: "Crimson Text", serif; font-size: 8.6px; line-height: 10.5px; color: var(--pink); }
  .bio--first { top: 350px; }
  .bio--first .bio__label { padding-left: 46px; }
  .bio--second { top: 473px; }
  .bio--second .bio__label { padding-left: 67px; }

  /* spine */
  .spine-text { position: absolute; margin: 0; writing-mode: vertical-rl; white-space: nowrap; line-height: 1; }
  .spine-title { left: 42px; top: 180px; font-size: 48px; font-family: "Dancing Script", cursive; font-weight: 600; color: var(--pink); }
  .spine-subtitle { left: 12px; top: 222px; font-size: 17px; font-family: "Marcellus", serif; color: var(--pink); }

  /* front */
  .frame-lines { position: absolute; left: 0; top: 0; }
  .front-title { left: 40px; top: 100px; width: 400px; text-align: center; font-size: 62px; }
  .front-subtitle { left: 90px; top: 203px; width: 300px; text-align: center; font-size: 24px; color: var(--white-soft); }
  .authors { position: absolute; left: 90px; top: 521px; width: 300px; text-align: center; font-family: "Marcellus", serif; }
  .authors__label { margin: 0 0 2px; font-size: 16px; color: var(--cream-text); line-height: 1.1; }
  .authors__name { margin: 0; font-size: 22px; color: var(--pink); line-height: 1.05; }
  .authors__amp { margin: 0; font-size: 19px; color: var(--pink); line-height: 1; }
</style>
</head>
<body>
<div class="canvas">

  <svg class="flap" width="1200" height="80" viewBox="0 0 1200 80" aria-hidden="true">
    <polygon points="62,20 606,62 1138,20 1138,78 62,78" fill="var(--cream)"/>
  </svg>

  <section class="panel panel--back" aria-label="Back cover">
    <div class="art" role="img" aria-label="Line drawing of an open hanging birdcage with a dove flying out of its door" style="left:173px; top:7px; width:214px; height:200px;"></div>
    <h2 class="script-title back-title">Unbound Hearts</h2>
    <p class="subtitle back-subtitle">Called Out to Walk Open</p>

    <div class="bio bio--first">
      <p class="bio__label">Biografhy</p>
      <h3 class="bio__name">Dr. Martin Oskerby</h3>
      <p class="bio__text">Book cover for a study guide on Galatians. The title would be:<br>"Unbound Hearts: Called Out to Walk Open" Possibly using a bird breaking free from a cage.+<br>Book cover for a study guide on Galatians. The title would be:<br>"Unbound Hearts: Called Out to Walk Open" Possibly using a bird breaking free from a cage.+</p>
    </div>

    <div class="bio bio--second">
      <p class="bio__label">Biografhy</p>
      <h3 class="bio__name">Dr. Helen Oskerby</h3>
      <p class="bio__text">Book cover for a study guide on Galatians. The title would be:<br>"Unbound Hearts: Called Out to Walk Open" Possibly using a bird breaking free from a cage.+<br>Book cover for a study guide on Galatians. The title would be:<br>"Unbound Hearts: Called Out to Walk Open" Possibly using a bird breaking free from a cage.+</p>
    </div>
  </section>

  <section class="panel panel--spine" aria-label="Spine">
    <div class="art" role="img" aria-label="Dove in flight with motion lines" style="left:12px; top:66px; width:100px; height:90px;"></div>
    <p class="spine-text spine-title">Unbound Hearts</p>
    <p class="spine-text spine-subtitle">Called Out to Walk Open</p>
    <div class="art" role="img" aria-label="Dove in flight with motion lines" style="left:12px; top:474px; width:100px; height:90px;"></div>
  </section>

  <section class="panel panel--front" aria-label="Front cover">
    <svg class="frame-lines" width="481" height="633" viewBox="0 0 481 633" aria-hidden="true">
      <g stroke="var(--rose-line)" stroke-width="1.6" fill="none">
        <path d="M183 0 V127 H0"/>
        <path d="M298 0 V127 H481"/>
        <path d="M0 240 H183 V520"/>
        <path d="M481 240 H298 V520"/>
        <path d="M197 0 V127"/>
        <path d="M284 0 V127"/>
        <path d="M197 240 V300"/>
        <path d="M284 240 V520"/>
        <path d="M183 612 V633 M197 612 V633 M284 612 V633 M298 612 V633"/>
      </g>
    </svg>
    <div class="art" role="img" aria-label="Small hanging ring ornament on a string" style="left:222px; top:63px; width:37px; height:56px;"></div>
    <h1 class="script-title front-title">Unbound Hearts</h1>
    <p class="subtitle front-subtitle">Called Out to Walk Open</p>
    <div class="art" role="img" aria-label="Dove flying upward with motion lines" style="left:154px; top:240px; width:175px; height:153px;"></div>
    <div class="art" role="img" aria-label="Pink flower sprig with leaves" style="left:208px; top:362px; width:66px; height:140px;"></div>

    <div class="authors">
      <p class="authors__label">Authors are :</p>
      <p class="authors__name">Dr. Martin Oskerby</p>
      <p class="authors__amp">&amp;</p>
      <p class="authors__name">Dr. Helen Oskerby</p>
    </div>
  </section>

</div>
</body>
</html>
```